Brookhurst Dental Care
Daniel K. Pruitt DMD
Professional
5283 E. Copper Ridge Ave, Suite B-4
Phoenix, AZ 85019
office@brookhurstdental.com
www.brookhurstdental.com
Please incorporate my name:
under the Brookhurst Dental Care logo
Use standard format to write in scheduled appointments.
Also include at bottom:
"We appreciate a 24 hr. notice for cancellations"

```html
<!DOCTYPE html>
<html lang="en">
<head>
<meta charset="utf-8">
<title>Brookhurst Dental Care — Stationery</title>
<link rel="stylesheet" href="https://fonts.googleapis.com/css2?family=Cinzel:wght@600&family=Lato:wght@400;700&display=swap">
<style>
  :root {
    --green: #1f7a4b;
    --green-soft: #3a8e62;
    --paper: #ffffff;
    --ink: #4a4f4c;
    --muted: #8a908c;
    --backdrop: #e4e6e5;
    --line: #c9cdca;
  }
  * { box-sizing: border-box; margin: 0; padding: 0; }
  html, body { width: 1200px; height: 881px; overflow: hidden; }
  body {
    background: var(--backdrop);
    position: relative;
    font-family: "Lato", Arial, sans-serif;
    color: var(--ink);
  }
  .piece {
    position: absolute;
    background: var(--paper);
    box-shadow: 0 2px 10px rgba(0,0,0,.12);
    overflow: hidden;
  }
  /* Header area reserved for the decorative band, rendered as a soft flat fill */
  .header-fill {
    position: absolute; left: 0; top: 0; width: 100%;
    background: linear-gradient(180deg, var(--green) 0%, var(--green-soft) 100%);
  }

  .logo { text-align: center; color: var(--green); font-family: "Cinzel", Georgia, serif; font-weight: 600; }
  .logo-name { display: block; letter-spacing: .02em; line-height: 1; }
  .logo-sub { display: block; letter-spacing: .42em; line-height: 1; margin-top: .35em; }
  .doctor { color: var(--ink); font-size: 12px; text-align: center; font-weight: 700; }

  /* Folder cover */
  .folder { left: 60px; top: 60px; width: 300px; height: 430px; }
  .folder .header-fill { height: 90px; }
  .folder .logo { position: absolute; left: 0; right: 0; top: 200px; }
  .folder .logo-name { font-size: 30px; }
  .folder .logo-sub { font-size: 11px; }

  /* Letterhead */
  .letterhead { left: 410px; top: 60px; width: 310px; height: 420px; }
  .letterhead .header-fill { height: 48px; }
  .letterhead .logo { position: absolute; left: 22px; top: 82px; text-align: left; }
  .letterhead .logo-name { font-size: 18px; }
  .letterhead .logo-sub { font-size: 7px; }
  .letterhead .body-lines { position: absolute; left: 22px; right: 22px; top: 150px; }
  .letterhead .body-lines span { display: block; height: 4px; background: #eceeed; margin-bottom: 10px; border-radius: 2px; }
  .letterhead .body-lines span.short { width: 62%; }
  .letterhead .footer {
    position: absolute; left: 0; right: 0; bottom: 0; height: 34px;
    border-top: 3px solid var(--green);
    font-size: 8px; text-align: center; padding-top: 7px; line-height: 1.4; color: var(--muted);
  }

  /* Envelope */
  .envelope { left: 770px; top: 60px; width: 380px; height: 190px; }
  .envelope .header-fill { height: 30px; }
  .envelope .logo { position: absolute; left: 18px; top: 54px; text-align: left; }
  .envelope .logo-name { font-size: 15px; }
  .envelope .logo-sub { font-size: 6px; }
  .envelope .return { position: absolute; left: 18px; top: 92px; font-size: 8px; line-height: 1.45; color: var(--muted); font-style: normal; }

  /* Wall sign */
  .sign {
    left: 770px; top: 290px; width: 380px; height: 230px;
    background: rgba(255,255,255,.55);
    border: 1px solid #fff;
    box-shadow: 0 2px 12px rgba(0,0,0,.12), inset 0 0 0 6px rgba(255,255,255,.4);
    display: flex; align-items: center; justify-content: center;
  }
  .sign .stud { position: absolute; width: 14px; height: 14px; border-radius: 50%; background: #d6dad8; border: 2px solid #f4f5f4; }
  .sign .stud.tl { left: 16px; top: 16px; } .sign .stud.tr { right: 16px; top: 16px; }
  .sign .stud.bl { left: 16px; bottom: 16px; } .sign .stud.br { right: 16px; bottom: 16px; }
  .sign .logo { color: #7d8581; }
  .sign .logo-name { font-size: 32px; }
  .sign .logo-sub { font-size: 11px; }

  /* Business cards */
  .card { top: 580px; width: 340px; height: 200px; }
  .card .header-fill { height: 36px; }
  .card-front { left: 60px; }
  .card-front .logo { position: absolute; left: 0; right: 0; top: 66px; }
  .card-front .logo-name { font-size: 22px; }
  .card-front .logo-sub { font-size: 8px; }
  .card-front .doctor { position: absolute; left: 0; right: 0; top: 112px; }
  .card-front .contact {
    position: absolute; left: 0; right: 0; bottom: 12px;
    text-align: center; font-size: 8.5px; line-height: 1.45; color: var(--muted);
  }
  .card-back { left: 440px; }
  .card-back .heading {
    position: absolute; left: 22px; top: 60px;
    font-family: "Cinzel", Georgia, serif; font-weight: 600; color: var(--green); font-size: 14px; letter-spacing: .08em;
  }
  .card-back .fields { position: absolute; left: 22px; right: 22px; top: 88px; }
  .card-back .field { display: flex; align-items: flex-end; gap: 8px; font-size: 10px; margin-bottom: 12px; }
  .card-back .field .rule { flex: 1; border-bottom: 1px solid var(--line); height: 10px; }
  .card-back .notice {
    position: absolute; left: 0; right: 0; bottom: 0; height: 28px;
    background: var(--green); color: #fff; font-size: 9.5px; text-align: center; line-height: 28px; font-style: italic;
  }
</style>
</head>
<body>

  <!-- Presentation folder -->
  <section class="piece folder">
    <div class="header-fill" role="img" aria-label="Decorative green header band"></div>
    <div class="logo">
      <span class="logo-name">BROOKHURST</span>
      <span class="logo-sub">DENTAL CARE</span>
    </div>
  </section>

  <!-- Letterhead -->
  <section class="piece letterhead">
    <div class="header-fill" role="img" aria-label="Decorative green header band"></div>
    <div class="logo">
      <span class="logo-name">BROOKHURST</span>
      <span class="logo-sub">DENTAL CARE</span>
    </div>
    <div class="body-lines" aria-hidden="true">
      <span></span><span></span><span></span><span class="short"></span>
      <span></span><span></span><span class="short"></span>
    </div>
    <footer class="footer">
      5283 E. Copper Ridge Ave, Suite B-4 &middot; Phoenix, AZ 85019<br>
      office@brookhurstdental.com &middot; www.brookhurstdental.com
    </footer>
  </section>

  <!-- Envelope -->
  <section class="piece envelope">
    <div class="header-fill" role="img" aria-label="Decorative green header band"></div>
    <div class="logo">
      <span class="logo-name">BROOKHURST</span>
      <span class="logo-sub">DENTAL CARE</span>
    </div>
    <address class="return">
      5283 E. Copper Ridge Ave, Suite B-4<br>
      Phoenix, AZ 85019
    </address>
  </section>

  <!-- Acrylic wall sign -->
  <section class="piece sign">
    <span class="stud tl"></span><span class="stud tr"></span>
    <span class="stud bl"></span><span class="stud br"></span>
    <div class="logo">
      <span class="logo-name">BROOKHURST</span>
      <span class="logo-sub">DENTAL CARE</span>
    </div>
  </section>

  <!-- Business card, front -->
  <section class="piece card card-front">
    <div class="header-fill" role="img" aria-label="Decorative green header band"></div>
    <div class="logo">
      <span class="logo-name">BROOKHURST</span>
      <span class="logo-sub">DENTAL CARE</span>
    </div>
    <p class="doctor">Daniel K. Pruitt DMD</p>
    <p class="contact">
      5283 E. Copper Ridge Ave, Suite B-4, Phoenix, AZ 85019<br>
      office@brookhurstdental.com &middot; www.brookhurstdental.com
    </p>
  </section>

  <!-- Business card, back: appointment -->
  <section class="piece card card-back">
    <div class="header-fill" role="img" aria-label="Decorative green header band"></div>
    <h2 class="heading">Appointment</h2>
    <div class="fields">
      <div class="field">Date <span class="rule"></span></div>
      <div class="field">Time <span class="rule"></span></div>
    </div>
    <p class="notice">We appreciate a 24 hr. notice for cancellations</p>
  </section>

</body>
</html>
```